・メインで紹介していただく2つのアクティビティーの情報は
以下のHPアドレスにございます。
https://kurumi-lodge.example.jp/wp/activities/星あかりの小径/
https://kurumi-lodge.example.jp/wp/activities/ムーンライトトレック/

・写真素材はグーグルのマイドライブ↓に格納いたしました
https://files.example.net/open?id=8XqPzLmTr2WvNc4Ka7bYdE1hJsG9uFoRt

・写真素材についてはトリミングも含め自由にお使いいただけます。デザインによっては数枚省いていただいても結構です。
~写真の説明~
1「山岳学舎を取り巻く山々」×2のどちらか :山岳学舎施設が山の中にあるというイメージを前面に押し出して頂きたい。
2「山岳学舎紹介・・・・」の写真は施設情報のところで小さくお使いください
そのなかでも「スカイランタン」と「スノースライダー」は こんなこともや
っているよ!程度の小さな丸切り抜きで添えてもらえれば結構です。

・納期期限:10月4日厳守でお願いします。作成過程で、連絡を取りながら作成していただける方を優先させていただきたいと存じます。
【星あかりの小径】
■催行期間 2019年 12月 14日(土)~2020年 4月5日(日) 一日3回
■料  金 小学生以上2,000円(スノーシューレンタル料込)/ 未就学児童 550円  ★山岳学舎ご宿泊者は1,000円 / 未就学児童 無料!!
【ムーンライトトレック】
■催行期間 2019年12月28日~2020年1月5日毎日
2,019年1月11日~3月22日までの土日祝祭日のみ  一日2回
■料  金 小学生以上3,800円(スノーシューレンタル料込)

<施設情報>くるみ原山岳学舎
宿泊 お一人様10,900円~(1泊2食)」〒503-2417 岐阜県大野郡白川村桐ヶ平518
05769-3-4072 https://kurumi-lodge.example.jp/ info@kurumi-gakusha.example

```html
<!DOCTYPE html>
<html lang="ja">
<head>
<meta charset="utf-8">
<title>白川郷で雪と遊ぼう。</title>
<link rel="stylesheet" href="https://fonts.googleapis.com/css2?family=M+PLUS+Rounded+1c:wght@500;800&family=Noto+Sans+JP:wght@400;700;900&display=swap">
<style>
:root{
  --blue:#1769bd;
  --blue-dark:#0f4c8c;
  --sky:#8fc0e8;
  --snow:#f4f8fc;
  --ink:#1d2a3a;
  --muted:#4a5a6c;
  --paper:#ffffff;
}
*{margin:0;padding:0;box-sizing:border-box}
html,body{width:851px;height:1200px;overflow:hidden;background:var(--paper)}
body{font-family:"Noto Sans JP",sans-serif;color:var(--ink);position:relative}
.hero{position:absolute;left:0;top:0;width:851px;height:728px;
  background:linear-gradient(180deg,#6fa8d8 0%,#b9d7ef 38%,#e9f1f8 62%,#ffffff 100%)}
.hero-person{position:absolute;left:250px;top:150px;width:290px;height:500px;border-radius:40px;
  background:linear-gradient(180deg,#d9dde2 0%,#e6c03c 35%,#d8a800 55%,#3b4150 80%,#eef3f8 100%);opacity:.85}
.title{position:absolute;left:40px;top:236px;transform:rotate(-24deg);transform-origin:left bottom;
  font-family:"M PLUS Rounded 1c",sans-serif;font-weight:800;font-size:54px;line-height:1;
  color:var(--blue);-webkit-text-stroke:8px #fff;paint-order:stroke fill;white-space:nowrap}
.inset{position:absolute;border:4px solid #fff;box-shadow:0 2px 6px rgba(0,0,0,.2)}
.inset-group{left:570px;top:130px;width:250px;height:120px;background:linear-gradient(180deg,#9cc4e6,#eef4fa)}
.inset-row{left:580px;top:400px;width:240px;height:110px;background:linear-gradient(180deg,#c8d6e4,#f5f8fb)}
.inset-woods{left:30px;top:360px;width:190px;height:130px;background:linear-gradient(180deg,#7d8f80,#eef2f0)}
.circle{position:absolute;width:125px;height:125px;border-radius:50%;border:4px solid #fff;box-shadow:0 2px 6px rgba(0,0,0,.2)}
.circle-slider{left:50px;top:545px;background:linear-gradient(180deg,#87b6de,#f1f6fa)}
.circle-lantern{left:670px;top:540px;background:radial-gradient(circle at 50% 40%,#f4b54a,#2a3d66 70%)}
.circle-label{position:absolute;font-size:15px;font-weight:700;color:var(--ink);text-shadow:0 0 3px #fff,0 0 3px #fff}
.label-slider{left:52px;top:676px}
.label-lantern{left:685px;top:670px}

.programs{position:absolute;left:30px;top:736px;width:791px;display:flex;gap:24px}
.program{flex:1}
.program-head{background:var(--blue);color:#fff;font-weight:700;font-size:17px;padding:3px 12px;border-radius:4px 4px 0 0;display:inline-block}
.program-body{border-top:3px solid var(--blue);padding-top:6px}
.dates{color:var(--blue);font-weight:900;line-height:1;display:flex;align-items:flex-end;gap:4px;white-space:nowrap}
.date{display:inline-flex;flex-direction:column}
.dates .year{font-size:11px;color:var(--muted);margin-bottom:2px}
.dates .big{font-size:34px}
.dates .small{font-size:13px;color:var(--ink);font-weight:700;padding-bottom:3px}
.fee{margin-top:8px;display:flex;gap:8px;align-items:flex-start}
.fee-tag{background:var(--blue);color:#fff;font-size:13px;font-weight:700;padding:4px 8px;border-radius:3px;white-space:nowrap}
.fee-text{font-size:13px;line-height:1.45;font-weight:700}
.fee-text .price{font-size:17px;color:var(--blue-dark)}
.sub-dates{font-size:12px;font-weight:700;margin-top:4px}
.notes{margin-top:8px;font-size:10.5px;line-height:1.5;color:var(--muted);list-style:none}
.notes li::before{content:"●";color:var(--blue);margin-right:3px}

.stay{position:absolute;left:30px;top:950px;width:791px;border-top:2px solid var(--blue);padding-top:8px;display:flex;align-items:baseline;gap:12px}
.stay-label{font-size:13px;font-weight:700;color:#fff;background:var(--blue-dark);padding:2px 8px;border-radius:3px}
.stay-price{font-size:24px;font-weight:900;color:var(--ink)}
.stay-price small{font-size:13px;font-weight:700}
.address{position:absolute;left:30px;top:994px;font-size:11px;color:var(--muted)}

.brand{position:absolute;left:30px;top:1030px;display:flex;align-items:center;gap:12px}
.brand-mark{width:34px;height:34px;border-radius:50%;background:var(--ink)}
.brand-name{font-size:26px;font-weight:700;color:var(--ink);line-height:1.1}
.contact{position:absolute;left:30px;top:1090px;display:flex;align-items:center;gap:10px}
.tel{font-size:40px;font-weight:900;color:var(--blue);letter-spacing:1px;display:flex;align-items:center;gap:6px}
.tel small{font-size:18px}
.web{position:absolute;left:470px;top:1092px;font-size:11px;line-height:1.6;color:var(--muted)}
.footnote{position:absolute;left:30px;top:1150px;width:791px;font-size:9.5px;line-height:1.5;color:var(--muted);border-top:1px solid #c9d6e3;padding-top:6px}
</style>
</head>
<body>
<section class="hero" role="img" aria-label="雪山を背景にスノーシューで雪原を歩く女性の写真"></section>
<div class="hero-person" role="img" aria-label="黄色いジャケットでスノーシューを履いて歩く参加者"></div>
<div class="inset inset-woods" role="img" aria-label="雪の森を歩く参加者たちの写真"></div>
<div class="inset inset-group" role="img" aria-label="雪原を一列に歩くスノーシューの一行の写真"></div>
<div class="inset inset-row" role="img" aria-label="雪の中で並んで遊ぶ子どもたちの写真"></div>
<div class="circle circle-slider" role="img" aria-label="スノースライダーで滑る様子"></div>
<div class="circle-label label-slider">スノースライダー</div>
<div class="circle circle-lantern" role="img" aria-label="夜空に浮かぶスカイランタン"></div>
<div class="circle-label label-lantern">スカイランタン</div>
<h1 class="title">白川郷で雪と遊ぼう。</h1>

<main class="programs">
  <article class="program">
    <div class="program-head">星あかりの小径</div>
    <div class="program-body">
      <div class="dates"><span class="date"><span class="year">2019年</span><span class="big">12月14日</span></span><span class="small">(土)〜</span><span class="date"><span class="year">2020年</span><span class="big">4月5日</span></span><span class="small">(日) 一日3回</span></div>
      <div class="fee"><span class="fee-tag">料金</span>
        <p class="fee-text">小学生以上 <span class="price">2,000円</span>(スノーシューレンタル料込)<br>未就学児童 550円<br>★山岳学舎ご宿泊者は1,000円 / 未就学児童 無料!!</p></div>
      <ul class="notes">
        <li>ご予約は前日までにお電話でお願いします。</li>
        <li>防寒着・手袋・帽子をご用意ください。</li>
        <li>天候により内容を変更する場合があります。</li>
      </ul>
    </div>
  </article>
  <article class="program">
    <div class="program-head">ムーンライトトレック</div>
    <div class="program-body">
      <div class="dates"><span class="date"><span class="year">2019年</span><span class="big">12月28日</span></span><span class="small">〜</span><span class="date"><span class="year">2020年</span><span class="big">1月5日</span></span><span class="small">毎日</span></div>
      <p class="sub-dates">2020年1月11日〜3月22日までの土日祝祭日のみ 一日2回</p>
      <div class="fee"><span class="fee-tag">料金</span>
        <p class="fee-text">小学生以上 <span class="price">3,800円</span>(スノーシューレンタル料込)</p></div>
      <ul class="notes">
        <li>集合は山岳学舎ロビーです。</li>
        <li>長靴は無料でお貸しします。</li>
        <li>小雨決行・荒天時は中止します。</li>
      </ul>
    </div>
  </article>
</main>

<div class="stay"><span class="stay-label">ご宿泊</span><span class="stay-price">お一人様 10,900円〜<small>(1泊2食)</small></span></div>
<p class="address">〒503-2417 岐阜県大野郡白川村桐ヶ平518</p>

<div class="brand"><span class="brand-mark"></span><div><div class="brand-name">Kurumihara Mountain School</div><div class="brand-name">くるみ原山岳学舎</div></div></div>

<div class="contact"><div class="tel"><svg width="30" height="30" viewBox="0 0 24 24" aria-hidden="true"><path fill="#1769bd" d="M6.6 10.8a15 15 0 0 0 6.6 6.6l2.2-2.2c.3-.3.7-.4 1-.2 1.1.4 2.3.6 3.6.6.6 0 1 .4 1 1V20c0 .6-.4 1-1 1A17 17 0 0 1 3 4c0-.6.4-1 1-1h3.5c.6 0 1 .4 1 1 0 1.3.2 2.5.6 3.6.1.3 0 .7-.2 1z"/></svg><small>TEL.</small>05769-3-4072</div></div>
<p class="web">https://kurumi-lodge.example.jp/<br>info@kurumi-gakusha.example</p>

<p class="footnote">山岳学舎は白川郷の山あいにある体験施設です。四季を通じて自然体験プログラムを行っています。お気軽にお問い合わせください。</p>
</body>
</html>
```